K & R Acreage Works. Business card design

We need a business card designed for a new business. We have a bulldozer and tractor service. We clear land and make wildlife food plots. We provide disking, bush hogging, and site prep services.
I have attached an image of a business card that I like and would like my business cards to look similar.

Target Market(s)

anyone needing bulldozer and/or tractor services

Industry/Entity Type

Business

Contact Information for Business Card

K & R Acreage Works, Operated by 7-M-Ranch
Doug Pelham
601-473-5826
dpr4178@mailvexo.com

Font styles to use
Sans Serif

Colors

Designer to choose colors to be used in the design.

Requirements
Must have
• image of tractor and bulldozer
• Land Clearing
• Wildlife food plots
• Bush Hogging
• Disking
• Site prep
Nice to have
• i have included a image of a business card that i like. I would like mine to be similar.

```html
<!DOCTYPE html>
<html lang="en">
<head>
<meta charset="utf-8">
<title>K &amp; R Acreage Works – Business Card</title>
<link rel="stylesheet" href="https://fonts.googleapis.com/css2?family=Roboto:wght@400;500&family=Roboto+Condensed:wght@700&display=swap">
<style>
  :root{
    --page:#e4e4e2;
    --card:#f3f3f1;
    --olive:#8f9233;
    --olive-band:#989a3c;
    --brown:#6b3d17;
    --frame:#6e3f17;
    --ink:#474747;
    --ink-dark:#2b2b2b;
    --rule:#d0d0cc;
  }
  *{margin:0;padding:0;box-sizing:border-box}
  html,body{width:1200px;height:771px;overflow:hidden}
  body{background:var(--page);font-family:"Roboto",sans-serif;position:relative}

  .card{
    position:absolute;left:300px;top:213px;width:600px;height:344px;
    background:var(--card);border-radius:16px;overflow:hidden;
    box-shadow:0 2px 6px rgba(0,0,0,.18);
  }

  .brand{position:absolute;left:48px;top:112px;display:flex;align-items:center;gap:7px}
  .brand-mark{width:22px;height:22px;background:var(--olive)}
  .brand-name{
    font-family:"Roboto Condensed",sans-serif;font-weight:700;font-size:23px;
    color:var(--brown);letter-spacing:.2px;line-height:1;text-transform:uppercase;
  }
  .tagline{
    position:absolute;left:48px;top:138px;
    font-family:"Roboto Condensed",sans-serif;font-weight:700;font-size:11.2px;
    color:var(--ink-dark);letter-spacing:.1px;text-transform:uppercase;
  }

  .photo{position:absolute;top:156px;height:89px;border:2px solid var(--frame)}
  .photo--dozer{left:46px;width:149px;background:linear-gradient(180deg,#7f9a6a 0%,#5d6e45 40%,#8d7b5a 75%,#6b5a3e 100%)}
  .photo--tractor{left:201px;width:119px;background:linear-gradient(180deg,#a7b38c 0%,#6f7f47 45%,#9a6a3a 70%,#6d6d3b 100%)}

  .divider{position:absolute;left:351px;top:70px;width:1px;height:214px;background:var(--rule)}

  .contact{position:absolute;left:381px;top:68px}
  .person-name{
    font-family:"Roboto Condensed",sans-serif;font-weight:700;font-size:22px;
    color:var(--olive);line-height:1.1;text-transform:uppercase;
  }
  .person-role{font-size:16px;font-weight:500;color:var(--brown);line-height:1.2;text-transform:uppercase;margin-top:1px}

  .details{list-style:none;margin-top:14px}
  .details li{display:flex;align-items:center;gap:7px;font-size:14.5px;color:var(--ink);height:18.5px}
  .details svg{width:13px;height:13px;fill:var(--olive);flex:none}

  .services-title{
    margin-top:12px;font-family:"Roboto Condensed",sans-serif;font-weight:700;font-size:18px;
    color:var(--olive);text-transform:uppercase;line-height:1.1;
  }
  .services{list-style:none;margin-top:1px}
  .services li{font-size:14.5px;color:var(--ink);height:18px;display:flex;align-items:center}
  .services li::before,.dot{content:"";display:inline-block;width:5px;height:5px;border-radius:50%;background:var(--olive);margin-right:7px}
  .dot{margin:0 5px 0 4px}

  .foot-line{position:absolute;left:0;right:0;top:323px;height:2px;background:var(--brown)}
  .foot-band{position:absolute;left:0;right:0;top:327px;bottom:0;background:var(--olive-band)}
</style>
</head>
<body>
  <main class="card">
    <div class="brand">
      <span class="brand-mark"></span>
      <span class="brand-name">K &amp; R Acreage Works</span>
    </div>
    <p class="tagline">For all of your land improvement needs</p>

    <div class="photo photo--dozer" role="img" aria-label="Photo of a yellow bulldozer pushing soil at a cleared site"></div>
    <div class="photo photo--tractor" role="img" aria-label="Photo of an orange tractor with a front loader in tall grass"></div>

    <div class="divider"></div>

    <section class="contact">
      <h1 class="person-name">Doug Pelham</h1>
      <p class="person-role">Owner</p>

      <ul class="details">
        <li><svg viewBox="0 0 24 24" aria-hidden="true"><path d="M6.6 10.8a15.1 15.1 0 0 0 6.6 6.6l2.2-2.2c.3-.3.7-.4 1-.2 1.1.4 2.3.6 3.6.6.6 0 1 .4 1 1V20c0 .6-.4 1-1 1A17 17 0 0 1 3 4c0-.6.4-1 1-1h3.5c.6 0 1 .4 1 1 0 1.3.2 2.5.6 3.6.1.3 0 .7-.2 1z"/></svg>601-473-5826</li>
        <li><svg viewBox="0 0 24 24" aria-hidden="true"><path d="M2 5h20v14H2z M2 5l10 8 10-8" fill="var(--olive)"/><path d="M3 6l9 7 9-7" fill="none" stroke="#f3f3f1" stroke-width="1.6"/></svg>dpr4178@mailvexo.com</li>
        <li><svg viewBox="0 0 24 24" aria-hidden="true"><circle cx="12" cy="12" r="10"/><path d="M7 7c2 0 3 1 3 3s-2 2-2 4 1 3 1 4M15 5c-1 2 0 3 2 4s2 3 1 5" fill="none" stroke="#f3f3f1" stroke-width="1.6"/></svg>kracreageworks.com</li>
      </ul>

      <h2 class="services-title">We Creaded</h2>
      <ul class="services">
        <li>Land Clearing</li>
        <li>Wildlife food plots</li>
        <li>Bush Hogging</li>
        <li>Disking<span class="dot"></span>Site prep</li>
      </ul>
    </section>

    <div class="foot-line"></div>
    <div class="foot-band"></div>
  </main>
</body>
</html>
```